Law practice business card

I have an existing logo that I would like to make a little cleaner and maybe something more creative, but using the same base. I would like a contempoary design of the business card.

Industry/Entity Type

Law

Logo Text

On one side of the card - below the logo - I would want to say "TOSPRAVO" and below that it should read "LAW OFFICES, PC" in smaller print. If you have somethign more creative, I would love to see it.

Logo styles of interest
Lettermark Logo
Font styles to use
Sans Serif

Colors

Designer to choose only greyscale colors for use in the design.

Requirements
Must have
• Standard info: My name with "Attorney at Law" underneath; phone, fax, address, email and website.

```html
<!DOCTYPE html>
<html lang="en">
<head>
<meta charset="utf-8">
<title>Tospravo Law Offices – Business Card</title>
<link rel="stylesheet" href="https://fonts.googleapis.com/css2?family=Cinzel:wght@500;700&family=Crimson+Text:wght@400;600&display=swap">
<style>
  :root {
    --backdrop: #2b2b2c;
    --card: #ffffff;
    --card-shade: #eeeeee;
    --wine: #3a1518;
    --ink: #2a2a2a;
    --muted: #8a8a8a;
    --rule: #9a9a9a;
    --faint: #e4e4e4;
    --faint-line: #d6d6d6;
  }
  * { box-sizing: border-box; margin: 0; padding: 0; }
  html, body { width: 1200px; height: 900px; overflow: hidden; }
  body {
    background: var(--backdrop);
    font-family: "Crimson Text", serif;
    position: relative;
  }
  .card {
    position: absolute;
    left: 270px;
    width: 660px;
    height: 377px;
    background: linear-gradient(120deg, var(--card) 0%, var(--card) 55%, var(--card-shade) 100%);
    overflow: hidden;
    box-shadow: 0 10px 30px rgba(0,0,0,0.5);
  }
  .card--front { top: 55px; }
  .card--back { top: 468px; }

  .backdrop-square {
    position: absolute;
    left: -60px;
    top: 60px;
    width: 360px;
    height: 360px;
    background: var(--faint);
    outline: 6px solid var(--card);
    box-shadow: 0 0 0 9px var(--faint-line);
  }

  .brand {
    position: absolute;
    right: 60px;
    top: 60px;
    width: 300px;
    text-align: center;
    color: var(--wine);
  }
  .brand__mark {
    display: block;
    width: 30px;
    height: 30px;
    margin: 0 auto 18px;
    background: var(--wine);
  }
  .brand__name {
    font-family: "Cinzel", serif;
    font-weight: 700;
    font-size: 50px;
    letter-spacing: 1px;
    line-height: 1;
  }
  .brand__tagline {
    display: flex;
    align-items: center;
    gap: 8px;
    margin-top: 6px;
    font-family: "Crimson Text", serif;
    font-size: 15px;
    letter-spacing: 1px;
    color: var(--ink);
  }
  .brand__tagline::before,
  .brand__tagline::after {
    content: "";
    flex: 1;
    height: 1px;
    background: var(--ink);
  }

  .card--back .brand { top: 34px; right: 40px; width: 270px; }
  .card--back .brand__name { font-size: 44px; }

  .contact {
    position: absolute;
    left: 48px;
    bottom: 28px;
    color: var(--ink);
  }
  .contact__name {
    font-family: "Cinzel", serif;
    font-weight: 700;
    font-size: 20px;
    color: var(--wine);
    letter-spacing: 0.5px;
  }
  .contact__role {
    font-size: 17px;
    color: var(--muted);
    margin-bottom: 12px;
  }
  .contact__list { list-style: none; }
  .contact__item {
    display: flex;
    align-items: center;
    gap: 10px;
    font-size: 17px;
    line-height: 22px;
  }
  .contact__item svg { width: 13px; height: 13px; fill: var(--wine); flex: none; }
  .contact__group + .contact__group { margin-top: 10px; }
  .contact__address {
    margin-top: 8px;
    padding-top: 6px;
    border-top: 1px solid var(--rule);
    width: 380px;
  }
</style>
</head>
<body>

<section class="card card--front" aria-label="Card front">
  <div class="backdrop-square" aria-hidden="true"></div>
  <div class="brand">
    <span class="brand__mark" aria-hidden="true"></span>
    <div class="brand__name">TOSPRAVO</div>
    <div class="brand__tagline">LAW OFFICES, PC</div>
  </div>
</section>

<section class="card card--back" aria-label="Card back">
  <div class="backdrop-square" aria-hidden="true"></div>
  <div class="brand">
    <span class="brand__mark" aria-hidden="true"></span>
    <div class="brand__name">TOSPRAVO</div>
    <div class="brand__tagline">LAW OFFICES, PC</div>
  </div>

  <div class="contact">
    <div class="contact__name">TOSPRAVO</div>
    <div class="contact__role">Attorney at Law</div>
    <ul class="contact__list contact__group">
      <li class="contact__item">
        <svg viewBox="0 0 16 16" aria-label="Phone"><path d="M2 5c0-2 2-3 6-3s6 1 6 3v1h-3V5H5v1H2zM4 7h8l2 7H2z"/></svg>
        (00) 0000 0000
      </li>
      <li class="contact__item">
        <svg viewBox="0 0 16 16" aria-label="Fax"><path d="M4 1h8v5H4zM2 7h12v7H2zM5 9h6v1H5zM5 11h6v1H5z"/></svg>
        (00) 0000 0000
      </li>
    </ul>
    <ul class="contact__list contact__group">
      <li class="contact__item">
        <svg viewBox="0 0 16 16" aria-label="Email"><path d="M1 4h14v9H1zM2 5l6 4 6-4v-.5H2z"/></svg>
        info@tospravo.com
      </li>
      <li class="contact__item">
        <svg viewBox="0 0 16 16" aria-label="Website"><circle cx="8" cy="8" r="7"/></svg>
        www.tospravo.com
      </li>
    </ul>
    <ul class="contact__list contact__address">
      <li class="contact__item">
        <svg viewBox="0 0 16 16" aria-label="Address"><path d="M8 1a5 5 0 0 1 5 5c0 4-5 9-5 9S3 10 3 6a5 5 0 0 1 5-5zm0 3a2 2 0 1 0 0 4 2 2 0 0 0 0-4z"/></svg>
        11 dummy city, 00 dummy place
      </li>
    </ul>
  </div>
</section>

</body>
</html>
```